International travel site frontpage redesign

We sell tours to Scandinavia through our website www.velmora-journeys.com. The website has become a bit old fashioned and we are in the process of making the website responsive. As you can see from the attached pictures the website will be wider with the responsive design, and our current design does not fit anymore.

Here is what we are looking for:
- A website that reflects a trustworthy and quality oriented company.
- Making the website more modern looking, but still recognisable (we want to keep the colours).
- keeping in mind that the age group of our customers are from 20-80 years old (most in their 60s).
- We want to remove the popular tours part and are instead looking to replace this with picture boxes the following subjects Scandinavia Specialist, Special Offers, Contact, Norway (or Norway Tours), Sweden (or Sweden Tours), Iceland (or Iceland Tours), Combination Tours. Possibly also Lapland, Winter, Northern Lights, Fjords and Capitals. Some of these categories can be smaller or perhaps half boxes; i.e. Winter and Northern lights in one. If we end up with four boxes per line perhaps we could add a social media box next to the three first ones.
- The above means that the left hand meny with Norway Tours, Sweden Tours etc will be redundant.
- we will add another line to the search Box (on the top): Destinations
- The top menu will have the same categories, but we need to add languages as the website will be in English and German.
- The footer must be changed
- We can take away the box to the right where it says "your window to booking the best of our world"

Reason: One of the decission makers had to go away on business last minute.

Target Market(s)

Travelling to Scandinavia is not low cost, so the website needs to appeal to those that can afford to travel to our destination.
The age group of our customers are from 20-80 years old (most in their 60s).

Industry/Entity Type

Travel

Number of Pages Required

1 page

Requirements
Should not have
• Flashy or cheap looking special offers...

```html
<!DOCTYPE html>
<html lang="en">
<head>
<meta charset="utf-8">
<title>Velmora Journeys – Tours to Scandinavia</title>
<link href="https://fonts.googleapis.com/css2?family=Roboto:ital,wght@0,400;0,500;0,700;1,400&display=swap" rel="stylesheet">
<style>
:root{
  --red:#a3090f;
  --red-dark:#8e070c;
  --text:#555;
  --heading:#333;
  --card:#f6f6f6;
  --line:#e2e2e2;
  --footer:#ececec;
  --footer-base:#e2e2e2;
  --white:#fff;
}
*{box-sizing:border-box;margin:0;padding:0}
html,body{width:678px;height:1200px;overflow:hidden}
body{font-family:"Roboto",Arial,sans-serif;color:var(--text);background:var(--white);position:relative}

.site-header{position:absolute;left:42px;top:0;width:594px;height:50px}
.brand{position:absolute;left:0;top:27px;display:flex;align-items:center;gap:6px;color:var(--red);font-size:13px;letter-spacing:1.5px;font-weight:400}
.brand-mark{width:10px;height:10px;background:var(--red)}
.header-search{position:absolute;right:0;top:18px;display:flex;align-items:center;font-size:7px}
.header-search .label{color:var(--red);margin-right:10px;letter-spacing:.2px}
.search-input{width:132px;height:19px;border:1px solid #ddd;background:#f7f7f7;color:#aaa;font-style:italic;padding:5px 6px}
.search-btn{width:20px;height:19px;background:#6b6b6b;display:flex;align-items:center;justify-content:center}
.lang{margin-left:10px;color:#888}
.lang b{color:var(--red);font-weight:500}

.main-nav{position:absolute;left:42px;top:51px;width:594px;height:22px;background:var(--red);display:flex;align-items:center;padding-left:10px;border-radius:1px}
.main-nav a{color:var(--white);font-size:6.5px;text-decoration:none;letter-spacing:.3px;margin-right:28px}

.hero{position:absolute;left:42px;top:76px;width:594px;height:214px;background:linear-gradient(#2f4865 0%,#5a7590 38%,#9aa6b2 50%,#e8ebee 62%,#d9dde1 100%)}
.hero-dots{position:absolute;right:14px;bottom:14px;display:flex;gap:3px}
.hero-dots span{width:5px;height:5px;border-radius:50%;background:#111}
.hero-dots span:first-child{background:var(--red)}
.search-panel{position:absolute;left:12px;top:14px;width:149px;height:186px;background:var(--white);padding:14px 12px;box-shadow:0 0 3px rgba(0,0,0,.3)}
.search-panel h2{color:var(--red);font-size:9.5px;font-weight:400;letter-spacing:.3px;margin-bottom:6px}
.field-label{font-size:6.5px;color:#444;margin:6px 0 3px}
.select{height:19px;border:1px solid #ddd;background:#f5f5f5;font-size:5.6px;font-style:italic;color:#888;padding:6px 7px;position:relative}
.select::after{content:"";position:absolute;right:6px;top:7px;border:3px solid transparent;border-top:4px solid #777}
.search-now{position:absolute;right:12px;bottom:16px;width:69px;height:23px;background:#2b2b2b;color:var(--white);font-size:6.5px;display:flex;align-items:center;justify-content:center;letter-spacing:.3px;border-radius:1px}

.card{position:absolute;width:137px;background:var(--card);border:1px solid var(--line);padding:7px}
.photo{display:block;width:100%}
.card .photo{height:88px}
.card h3{color:var(--red);font-size:9px;font-weight:400;margin:6px 0 4px}
.card p{font-size:6.1px;line-height:10.5px;color:#555}
.price{margin-top:9px;width:64px;height:21px;background:var(--red);color:var(--white);font-size:6.8px;display:flex;align-items:center;padding-left:7px;clip-path:polygon(0 0,100% 0,88% 50%,100% 100%,0 100%)}

.contact{position:absolute;left:346px;top:506px;width:290px;height:184px;background:var(--card);border:1px solid var(--line);padding:7px 7px}
.contact .photo{height:88px}
.contact h3{color:var(--red);font-size:9px;font-weight:400;margin:6px 0 4px}
.contact .company{font-size:6.5px;font-weight:500;color:#333}
.contact .addr{font-size:6.5px;color:#555;margin-top:2px}
.contact .tel,.contact .mail{font-size:6.5px;color:var(--red);margin-top:2px}
.contact .tel{margin-top:7px}
.direction{position:absolute;right:8px;top:114px;width:88px;height:21px;background:var(--red);color:var(--white);font-size:6.8px;display:flex;align-items:center;padding-left:7px;clip-path:polygon(0 0,100% 0,92% 50%,100% 100%,0 100%)}

.story{position:absolute;top:707px;width:137px;height:179px;background:var(--card);border:1px solid var(--line)}
.story .photo{height:102px}
.story-body{padding:9px 10px}
.story h3{color:var(--red);font-size:9px;font-weight:400;margin-bottom:4px}
.story p{font-size:6.1px;line-height:10.5px}
.read-more{display:block;margin-top:5px;font-size:6.3px;color:var(--red);letter-spacing:.2px}

.social-box{position:absolute;left:498px;top:707px;width:138px;height:179px;background:var(--card);border:1px solid var(--line);padding:9px 10px}
.social-box h3{color:var(--red);font-size:9px;font-weight:400}
.page-id{display:flex;gap:6px;margin-top:10px}
.page-badge{width:30px;height:30px;background:var(--white);border:1px solid var(--line);display:flex;align-items:center;justify-content:center}
.page-badge span{width:10px;height:10px;background:var(--red)}
.page-name{font-size:7px;color:var(--red);line-height:9.5px}
.like{display:inline-block;margin-top:2px;background:#3b5998;color:var(--white);font-size:5px;font-weight:700;padding:1px 4px}
.fans{display:grid;grid-template-columns:repeat(4,25px);gap:2px;margin-top:9px}
.fans span{height:25px;background:#6d5a52}
.fans span:nth-child(3n){background:#3d3a3a}
.fans span:nth-child(4n+2){background:#8f7465}
.fans span:last-child{background:#d5d9de}
.plugin{border-top:1px solid #ccc;margin-top:5px;padding-top:3px;font-size:4.5px;color:#777;display:flex;gap:3px;align-items:center}
.plugin i{width:5px;height:5px;background:#3b5998;display:inline-block}

.site-footer{position:absolute;left:0;top:902px;width:678px;height:234px;background:var(--footer);border-top:1px solid #d6d6d6;border-bottom:1px solid #d6d6d6}
.fcol{position:absolute;top:22px}
.fcol h4{font-size:7.4px;font-weight:500;color:#333;letter-spacing:.2px;margin-bottom:6px}
.fcol ul{list-style:none;margin-bottom:12px}
.fcol li{font-size:6.4px;color:#555;line-height:15.2px;white-space:nowrap}
.connect{position:absolute;left:534px;top:189px}
.connect h4{font-size:7.4px;font-weight:500;color:#333;margin-bottom:5px}
.connect .icons{display:flex;gap:3px}
.connect .icons span{width:17px;height:17px;border-radius:50%}
.base{position:absolute;left:0;top:1136px;width:678px;height:64px;background:var(--footer-base)}
.guarantee{position:absolute;left:456px;top:16px;width:44px;height:34px;border-radius:50%;border:2px solid #333}
.cards{position:absolute;left:515px;top:26px;display:flex;gap:6px}
.cards span{width:26px;height:15px;background:var(--white);border:1px solid #ccc}
.cards span:nth-child(2){background:#c9c9c9}
</style>
</head>
<body>

<header class="site-header">
  <div class="brand"><span class="brand-mark"></span>VELMORA JOURNEYS</div>
  <div class="header-search">
    <span class="label">SEARCH DESTINATIONS</span>
    <div class="search-input">Search...</div>
    <div class="search-btn">
      <svg width="9" height="9" viewBox="0 0 10 10"><circle cx="4" cy="4" r="3" fill="none" stroke="#fff" stroke-width="1.3"/><line x1="6.2" y1="6.2" x2="9.2" y2="9.2" stroke="#fff" stroke-width="1.5"/></svg>
    </div>
    <span class="lang"><b>EN</b> &nbsp;|&nbsp; GER</span>
  </div>
</header>

<nav class="main-nav">
  <a>HOME</a><a>FJORDS</a><a>CAPITALS</a><a>CRUISES</a><a>WINTER</a><a>PICTURES</a>
</nav>

<section class="hero" role="img" aria-label="Travellers on a snowy northern cliff top beside a globe monument overlooking the sea">
  <form class="search-panel">
    <h2>SEARCH DESTINATIONS</h2>
    <div class="field-label">Tour Type:</div>
    <div class="select">All tour types</div>
    <div class="field-label">Tour Selection:</div>
    <div class="select">All tour selection</div>
    <div class="field-label">Travel Period:</div>
    <div class="select">All Travel period</div>
    <div class="search-now">SEARCH NOW</div>
  </form>
  <div class="hero-dots"><span></span><span></span><span></span><span></span></div>
</section>

<article class="card" style="left:42px;top:310px;height:184px">
  <div class="photo" role="img" aria-label="Calm fjord reflecting snowy mountains" style="background:linear-gradient(#b7c2cc,#6f7b76 55%,#3f4a45)"></div>
  <h3>Scandinavia Specialist</h3>
  <p>Vestibulum ante ipsum primis in faucibus orci luctus et ultrices posuere cubilia ..</p>
  <div class="price">From € 499</div>
</article>
<article class="card" style="left:194px;top:310px;height:184px">
  <div class="photo" role="img" aria-label="Pink wildflowers in front of a fjord valley" style="background:linear-gradient(#7ea6c8,#6b8b6a 55%,#4b7a2e)"></div>
  <h3>Special Offers</h3>
  <p>Vestibulum ante ipsum primis in faucibus orci luctus et ultrices posuere cubilia ..</p>
  <div class="price">From € 499</div>
</article>
<article class="card" style="left:346px;top:310px;height:184px">
  <div class="photo" role="img" aria-label="Colourful wooden harbour houses under blue sky" style="background:linear-gradient(#3f86d4,#b9553f 45%,#7e3b2d)"></div>
  <h3>Norway Tours</h3>
  <p>Vestibulum ante ipsum primis in faucibus orci luctus et ultrices posuere cubilia ..</p>
  <div class="price">From € 499</div>
</article>
<article class="card" style="left:498px;top:310px;height:184px">
  <div class="photo" role="img" aria-label="Red brick castle with towers by the water" style="background:linear-gradient(#2f73c9,#a8503d 55%,#5d3a2b)"></div>
  <h3>Sweden Tours</h3>
  <p>Vestibulum ante ipsum primis in faucibus orci luctus et ultrices posuere cubilia ..</p>
  <div class="price">From € 499</div>
</article>

<article class="card" style="left:42px;top:506px;height:184px">
  <div class="photo" role="img" aria-label="Snow covered cars in a town parking lot" style="background:linear-gradient(#a9b0b8,#d7dade 55%,#eef0f2)"></div>
  <h3>Iceland Tours</h3>
  <p>Vestibulum ante ipsum primis in faucibus orci luctus et ultrices posuere cubilia ..</p>
  <div class="price">From € 499</div>
</article>
<article class="card" style="left:194px;top:506px;height:184px">
  <div class="photo" role="img" aria-label="Red mountain railway train on a green slope" style="background:linear-gradient(#5a7a3a,#b9bcbf 50%,#3e5a2c)"></div>
  <h3>Combination Tours</h3>
  <p>Vestibulum ante ipsum primis in faucibus orci luctus et ultrices posuere cubilia ..</p>
  <div class="price">From € 499</div>
</article>

<article class="contact">
  <div class="photo" role="img" aria-label="Map of southern Norway" style="background:linear-gradient(90deg,#b8d4e6,#cfe0c8 30%,#c6dcb6 70%,#dce5cf)"></div>
  <h3>Contact Us</h3>
  <div class="company">Velmora Journeys AS</div>
  <div class="addr">Lindeveien 14, N-0571 Oslo, Norway</div>
  <div class="tel">+47 21 55 08 42</div>
  <div class="mail">info@velmora-journeys.com</div>
  <div class="direction">Get Full Direction</div>
</article>

<article class="story" style="left:42px">
  <div class="photo" role="img" aria-label="Horse drawn carriage beside a turf roofed farmhouse" style="background:linear-gradient(#9fc0dc,#6f9a4c 50%,#5b7f3a)"></div>
  <div class="story-body">
    <h3>About Lapland</h3>
    <p>Aliquam molestie, mi et imperdiet euismod, dui purus auctor tellus, et interdum lacus lectus etmagna,.</p>
    <span class="read-more">READ MORE</span>
  </div>
</article>
<article class="story" style="left:194px">
  <div class="photo" role="img" aria-label="Harbour town lit up on a blue winter evening" style="background:linear-gradient(#24407a,#3a5a9a 45%,#8a6a4a 70%,#2b3f6a)"></div>
  <div class="story-body">
    <h3>Winter, Northern Lights</h3>
    <p>Aliquam molestie, mi et imperdiet euismod, dui purus auctor tellus, et interdum lacus lectus etmagna,.</p>
    <span class="read-more">READ MORE</span>
  </div>
</article>
<article class="story" style="left:346px">
  <div class="photo" role="img" aria-label="Cyclists on a gravel road through a green gorge" style="background:linear-gradient(#6f8a5a,#aab0a4 55%,#57723f)"></div>
  <div class="story-body">
    <h3>Fjords and Capitals</h3>
    <p>Aliquam molestie, mi et imperdiet euismod, dui purus auctor tellus, et interdum lacus lectus etmagna,.</p>
    <span class="read-more">READ MORE</span>
  </div>
</article>

<aside class="social-box">
  <h3>Find us on Friendbook</h3>
  <div class="page-id">
    <div class="page-badge"><span></span></div>
    <div class="page-name">Velmora<br>Journeys AS<br><span class="like">Like</span></div>
  </div>
  <div class="fans" role="img" aria-label="Profile pictures of followers">
    <span></span><span></span><span></span><span></span>
    <span></span><span></span><span></span><span></span>
    <span></span><span></span><span></span><span></span>
  </div>
  <div class="plugin"><i></i>Friendbook social plugin</div>
</aside>

<footer class="site-footer">
  <div class="fcol" style="left:42px">
    <h4>TOUR TYPE</h4>
    <ul><li>Tour Types</li><li>Escorted Coach Tours</li><li>Independent Rail Tours</li><li>Independent Short Breaks</li><li>Partly Escorted Tours</li><li>Scandinavian Cruises</li><li>Self Drive Tours</li></ul>
    <h4>RECENTLY ADDED TOURS</h4>
    <ul><li>Baltic &amp; Russian Explorer</li><li>Iceland Wilderness</li><li>Baltic Classical</li></ul>
  </div>
  <div class="fcol" style="left:153px">
    <h4>WINTER TOUR TYPES</h4>
    <ul><li>Norway Winter Tours</li><li>Sweden Winter Tours</li><li>Finland Winter Tours</li><li>Iceland Winter Tours</li></ul>
    <h4>WINTER SELECTIONS</h4>
    <ul><li>Norway Winter Cruises</li><li>Ice Hotel Holidays</li><li>Winter Rail Tours</li><li>Lapland Winter Tours</li><li>Winter Weekend Breaks</li><li>Winter Tours Unpolished</li></ul>
  </div>
  <div class="fcol" style="left:268px">
    <h4>RECENTLY UPDATED TOURS</h4>
    <ul><li>Northern Lights Cruise</li><li>Lapland Winter Adventure</li><li>Pine Lodge, Northern Lights &amp; Tromsø</li></ul>
    <h4>VELMORA JOURNEYS</h4>
    <ul><li>About Velmora Journeys</li><li>Booking and Payment Procedure</li><li>Terms and Conditions</li><li>Frequently Asked Questions (FAQ)</li><li>Travel Experiences</li><li>Photo Credits</li><li>Site Map</li><li>Contact</li></ul>
  </div>
  <div class="fcol" style="left:417px">
    <h4>TOUR SELECTIONS</h4>
    <ul><li>Fjord Tours</li><li>Scandinavian Capitals</li><li>Scandinavia Cruise Packages</li><li>Exclusive Tours</li><li>Midnight Sun</li><li>Activity Tours</li></ul>
  </div>
  <div class="fcol" style="left:534px">
    <h4>&nbsp;</h4>
    <ul><li>Meet the locals</li><li>Northern lights</li><li>Norway Tours</li><li>Sweden Tours</li><li>Iceland Tours</li><li>Göta Canal Cruises</li><li>Coastal Express Cruises</li></ul>
  </div>
  <div class="connect">
    <h4>CONNECT US</h4>
    <div class="icons">
      <span style="background:#3b5998"></span><span style="background:#2fa9d8"></span><span style="background:#c8232c"></span><span style="background:#8a6a4c"></span><span style="background:#c4302b"></span>
    </div>
  </div>
</footer>

<div class="base">
  <div class="guarantee"></div>
  <div class="cards"><span></span><span></span><span></span><span></span></div>
</div>

</body>
</html>
```